Create a basic website for a new air cargo consultancy, called 'Zephyrra Logistics'

We want to build a basic website (homepage, 'about us' page, services and contact us page).
We have a logo, we have most of the text to be inserted, but not all. We also still need to take pictures.
We would like to have a fresh and modern, but business like design and the creation of the website.
We want to be able to modify the website after (add pictures and more text, update references).
We already have a url.

```html
<!DOCTYPE html>
<html lang="en">
<head>
<meta charset="utf-8">
<title>Zephyrra Logistics — Air Cargo Consultancy</title>
<link href="https://fonts.googleapis.com/css2?family=Marcellus&family=Poppins:wght@400;500;600;700&display=swap" rel="stylesheet">
<style>
:root{
  --navy:#2b3494;
  --gold:#d9a02a;
  --gold-btn:#f0b02e;
  --ink:#1c1c1c;
  --muted:#4a4a4a;
  --white:#fff;
  --line:#c9cbe0;
}
*{box-sizing:border-box;margin:0;padding:0}
html,body{width:1200px;height:2886px;overflow:hidden}
body{position:relative;font-family:'Poppins',sans-serif;color:var(--ink);background:var(--white)}
.abs{position:absolute}
.serif{font-family:'Marcellus',serif}

/* header */
.topbar{left:448px;top:0;width:752px;height:50px;background:var(--navy);border-bottom-left-radius:30px}
.search{left:452px;top:0;width:224px;height:50px;background:var(--gold);border-radius:0 0 30px 30px;color:#fff;font-size:15px;padding:16px 0 0 40px}
.search-btn{left:600px;top:0;width:76px;height:50px;background:#b88416;border-radius:0 0 30px 0}
.contact-line{top:16px;color:#fff;font-size:14px;font-weight:500;display:flex;align-items:center;gap:10px}
.brand{left:140px;top:28px;display:flex;align-items:center;gap:10px;font-family:'Poppins',sans-serif;font-weight:600;font-size:30px;color:var(--gold)}
.brand-dot{width:18px;height:18px;border-radius:50%;background:var(--navy)}
.nav{top:78px;font-size:14px;font-weight:600;color:var(--ink)}
.nav.active{color:var(--navy);border-bottom:2px solid var(--navy);padding-bottom:2px}
.soc-top{top:73px;width:30px;height:30px;border-radius:50%;background:var(--gold)}

/* hero */
.hero{left:0;top:121px;width:1200px;height:551px;background:linear-gradient(180deg,#1d3c8a 0%,#3f6fb5 35%,#c7803f 68%,#5a3524 100%)}
.hero-ring{left:148px;top:191px;width:370px;height:370px;border-radius:50%;background:var(--gold)}
.hero-circle{left:166px;top:196px;width:354px;height:354px;border-radius:50%;background:var(--navy);color:#fff;text-align:center;padding-top:72px}
.hero-circle .small{font-size:30px}
.hero-circle .big{font-size:48px;line-height:52px}
.btn-white{display:inline-block;margin-top:26px;background:#fff;color:var(--navy);font-family:'Poppins',sans-serif;font-weight:600;font-size:14px;padding:12px 34px;border-radius:22px}
.dot{left:1119px;width:8px;height:8px;border-radius:50%;background:#fff}

/* about */
.about-bg{left:0;top:672px;width:1200px;height:791px;background:linear-gradient(180deg,#fff 0%,#f3f1f3 40%,#f4eeea 100%)}
.about-frame{left:170px;top:755px;width:409px;height:349px;border:2px solid var(--gold)}
.about-photo{left:199px;top:779px;width:410px;height:348px;background:linear-gradient(180deg,#c9c3b4 0%,#a99a7c 55%,#6b5a45 100%)}
.h-section{font-size:40px;color:var(--navy)}
.h-section .gold{color:var(--gold)}
.about-text{left:653px;top:860px;width:377px;font-size:14.5px;line-height:28px;color:var(--muted);text-align:justify}
.btn-gold{background:var(--gold-btn);color:#fff;font-weight:600;font-size:14px;border-radius:24px;display:flex;align-items:center;justify-content:center}
.card{top:1176px;width:272px;height:224px;background:#fff;border-radius:16px;box-shadow:0 4px 14px rgba(0,0,0,.08);overflow:hidden;padding:18px 14px 0 31px}
.card::before{content:"";position:absolute;left:0;top:0;width:17px;height:100%;background:var(--navy)}
.card.gold-edge::before{background:var(--gold)}
.card h3{font-size:18px;font-weight:600;margin-bottom:6px}
.card p{font-size:11.5px;line-height:19px;color:var(--muted);text-align:justify}

/* services */
.services-panel{left:0;top:1463px;width:600px;height:443px;background:var(--navy)}
.services-photo{left:600px;top:1463px;width:600px;height:443px;background:linear-gradient(180deg,#5f8cc4 0%,#c9a07a 45%,#d28a4e 65%,#8c6446 100%)}
.services-text{left:145px;top:1636px;width:372px;font-size:12.5px;line-height:23.3px;color:#fff;text-align:justify}

/* contact */
.contact-head{left:0;width:1200px;text-align:center}
.form-card{left:132px;top:2078px;width:932px;height:471px;background:#fff;box-shadow:0 4px 18px rgba(0,0,0,.1)}
.label{font-size:15px;color:var(--ink)}
.field{border:2px solid var(--line);border-radius:6px;height:43px;font-size:12px;padding:12px 10px;color:var(--ink);font-weight:500}

/* footer */
.footer{left:0;top:2627px;width:1200px;height:259px;background:var(--navy)}
.flink{top:2710px;color:#fff;font-weight:600;font-size:16px}
.fbrand{left:793px;top:2692px;text-align:right;width:260px;font-weight:600;font-size:44px;color:var(--gold);line-height:50px}
.fbrand-rule{left:722px;top:2763px;width:330px;height:1px;background:#5b63b0}
.fsoc{top:2813px;width:32px;height:32px;border-radius:50%;background:#fff;border:3px solid var(--gold)}
.copy{top:2820px;right:145px;color:#fff;font-size:14px}
</style>
</head>
<body>

<!-- header -->
<div class="abs topbar"></div>
<div class="abs search">Search......</div>
<div class="abs search-btn">
  <svg class="abs" style="left:30px;top:16px" width="16" height="16" viewBox="0 0 16 16"><circle cx="6.5" cy="6.5" r="5" fill="none" stroke="#fff" stroke-width="2"/><line x1="10.5" y1="10.5" x2="15" y2="15" stroke="#fff" stroke-width="2"/></svg>
</div>
<div class="abs contact-line" style="left:693px">
  <svg width="16" height="12" viewBox="0 0 16 12"><rect width="16" height="12" rx="1" fill="#fff"/><path d="M0 1 L8 7 L16 1" fill="none" stroke="#2b3494" stroke-width="1.5"/></svg>
  hello@zephyrralogistics.com
</div>
<div class="abs" style="left:909px;top:14px;width:1px;height:22px;background:#fff"></div>
<div class="abs contact-line" style="left:928px">
  <svg width="14" height="14" viewBox="0 0 24 24"><path fill="#fff" d="M6.6 10.8a15.1 15.1 0 0 0 6.6 6.6l2.2-2.2a1 1 0 0 1 1-.25 11.4 11.4 0 0 0 3.6.57 1 1 0 0 1 1 1V20a1 1 0 0 1-1 1A17 17 0 0 1 3 4a1 1 0 0 1 1-1h3.5a1 1 0 0 1 1 1c0 1.25.2 2.45.57 3.57a1 1 0 0 1-.25 1z"/></svg>
  +1 555 010 2040
</div>

<div class="abs brand"><span class="brand-dot"></span>Zephyrra</div>

<div class="abs nav active" style="left:496px">HOME</div>
<div class="abs nav" style="left:585px">ABOUT</div>
<div class="abs nav" style="left:678px">SERVICES</div>
<div class="abs nav" style="left:789px">CONTACT US</div>
<div class="abs soc-top" style="left:928px" aria-label="Social link"></div>
<div class="abs soc-top" style="left:978px" aria-label="Social link"></div>
<div class="abs soc-top" style="left:1025px" aria-label="Social link"></div>

<!-- hero -->
<div class="abs hero" role="img" aria-label="Cargo jet taking off over a runway at sunset"></div>
<div class="abs hero-ring"></div>
<div class="abs hero-circle serif">
  <div class="small">WELCOME TO</div>
  <div class="big">ZEPHYRRA<br>LOGISTICS</div>
  <span class="btn-white">GET STARTED</span>
</div>
<div class="abs dot" style="top:300px"></div>
<div class="abs dot" style="top:323px;background:var(--gold)"></div>
<div class="abs dot" style="top:347px"></div>

<!-- about -->
<div class="abs about-bg"></div>
<div class="abs about-frame"></div>
<div class="abs about-photo" role="img" aria-label="Cargo plane on the apron with netted pallets on a loader"></div>
<h2 class="abs h-section serif" style="left:653px;top:798px">ABOUT <span class="gold">US</span></h2>
<p class="abs about-text">At Zephyrra Logistics, we understand the unique challenges and opportunities within the air cargo industry. Our team of seasoned professionals offers in-depth expertise and tailored solutions to optimize your logistics operations, streamline processes, and improve efficiency. With a focus on</p>
<div class="abs btn-gold" style="left:653px;top:1052px;width:160px;height:44px">READ MORE</div>

<div class="abs card" style="left:143px">
  <h3>Digitalization</h3>
  <p>The core of our approach. We assist clients in adopting cutting-edge technologies to enhance visibility, improve communication, and automate workflows. By leveraging the latest digital tools, we help you stay ahead of the curve and meet the evolving demands of the market.</p>
</div>
<div class="abs card gold-edge" style="left:464px">
  <h3>Community building</h3>
  <p>Another key aspect of our consultancy. We believe in the power of collaboration and connectivity. Our initiatives are designed to strengthen relationships within the cargo community, fostering partnerships that drive innovation and growth.</p>
</div>
<div class="abs card" style="left:784px">
  <h3>Sustainability</h3>
  <p>Integral to our mission. We work with clients to develop and implement eco-friendly practices that reduce environmental impact and promote long-term sustainability. From optimizing fuel efficiency to exploring alternative energy sources, we are committed to helping you achieve</p>
</div>

<!-- services -->
<div class="abs services-panel"></div>
<div class="abs services-photo" role="img" aria-label="Airliner parked on a runway under an evening sky"></div>
<h2 class="abs serif" style="left:145px;top:1562px;font-size:50px;color:#fff"><span style="color:var(--gold)">OUR</span> SERVICES</h2>
<p class="abs services-text">Lorem ipsum dolor sit amet, consectetur adipiscing elit, sed do eiusmod tempor incididunt ut labore et dolore magna aliqua. Ut enim ad minim veniam, quis nostrud exercitation ullamco laboris nisi ut aliquip ex ea commodo consequat. Duis aute irure dolor in reprehenderit in voluptate velitqui officia deserunt mollit anim id est labor</p>
<div class="abs btn-gold" style="left:145px;top:1800px;width:135px;height:41px">READ MORE</div>

<!-- contact -->
<div class="abs form-card"></div>
<div class="abs contact-head serif" style="top:2008px;font-size:34px;color:var(--ink)">CONTACT</div>
<div class="abs contact-head serif" style="top:2048px;font-size:52px;color:var(--navy)"><span style="color:var(--gold)">GET IN</span> TOUCH</div>

<div class="abs label" style="left:178px;top:2148px">Name</div>
<div class="abs label" style="left:469px;top:2148px">Phone Number</div>
<div class="abs label" style="left:760px;top:2148px">Email</div>
<div class="abs field" style="left:172px;top:2176px;width:276px">John Doe</div>
<div class="abs field" style="left:464px;top:2176px;width:275px">+1555 010 2040</div>
<div class="abs field" style="left:754px;top:2176px;width:276px">info@abc.com</div>

<div class="abs label" style="left:178px;top:2231px">Current Address</div>
<div class="abs label" style="left:760px;top:2231px">Zip Code</div>
<div class="abs field" style="left:172px;top:2259px;width:567px">123 Lorem Ipsum</div>
<div class="abs field" style="left:754px;top:2259px;width:276px">90224</div>

<div class="abs label" style="left:178px;top:2313px">Comment</div>
<div class="abs field" style="left:172px;top:2340px;width:858px;height:84px">Type Here</div>

<div class="abs btn-gold" style="left:532px;top:2457px;width:136px;height:40px">SUBMIT</div>

<!-- footer -->
<div class="abs footer"></div>
<div class="abs flink" style="left:147px">HOME</div>
<div class="abs flink" style="left:236px">ABOUT US</div>
<div class="abs flink" style="left:357px">SERVICES</div>
<div class="abs flink" style="left:474px">CONTACT US</div>
<div class="abs fbrand">Zephyrra</div>
<div class="abs fbrand-rule"></div>

<div class="abs fsoc" style="left:149px" aria-label="Social link"></div>
<div class="abs fsoc" style="left:189px" aria-label="Social link"></div>
<div class="abs fsoc" style="left:230px" aria-label="Social link"></div>
<div class="abs fsoc" style="left:270px" aria-label="Social link"></div>
<div class="abs fsoc" style="left:311px" aria-label="Social link"></div>
<div class="abs copy">© 2024 Zephyrra Logistics. All rights reserved.Privacy &nbsp;&nbsp;|&nbsp;&nbsp; Terms of Use</div>

</body>
</html>
```